Business Card for Leadership Coaching Business
Red Stone Leadership Coaching
Business Card for Leadership Coaching Business - Consulting
Creative Brief
Professional
Marla Pennington, CHRL
Leadership Coach
372 Fenwick Crescent, Oakville, Ontario L6K 3R2
marla@redstoneleadcoach.example
www.redstoneleadcoach.example
I am starting up a new business for leadership coaching. I have a great new logo and now I am looking for a great business card.
PRNGraphics PRNGraphics
Good afternoon. Can you post the logo you want to use on your card?

```html
<!DOCTYPE html>
<html lang="en">
<head>
<meta charset="utf-8">
<title>Red Stone Leadership Coaching – Business Card</title>
<link rel="stylesheet" href="https://fonts.googleapis.com/css2?family=Open+Sans:wght@400;600;700&display=swap">
<style>
  :root {
    --backdrop: #e6e7e9;
    --band-top: #2a5a9a;
    --band-bottom: #163e78;
    --accent-line: #4d8fd1;
    --card-white: #ffffff;
    --card-fade: #eef0f3;
    --brand-blue: #1d4f91;
    --text-grey: #555a60;
    --divider: #c4c8cd;
    --icon-blue: #3d6fb0;
  }
  * { margin: 0; padding: 0; box-sizing: border-box; }
  html, body {
    width: 1200px; height: 780px; overflow: hidden;
    background: var(--backdrop);
    font-family: "Open Sans", Arial, sans-serif;
  }
  .canvas {
    position: relative; width: 1200px; height: 780px;
  }
  .business-card {
    position: absolute; left: 75px; top: 90px;
    width: 1050px; height: 600px;
    border-radius: 34px; overflow: hidden;
    background: linear-gradient(180deg, var(--card-white) 40%, var(--card-fade) 100%);
    box-shadow: 0 10px 28px rgba(0,0,0,0.18);
  }
  .header-band {
    position: absolute; left: 0; top: 0; width: 100%; height: 170px;
    background: linear-gradient(180deg, var(--band-top), var(--band-bottom));
    border-bottom: 7px solid var(--accent-line);
    text-align: center; color: #fff;
    padding-top: 42px;
  }
  .person-name { font-size: 40px; font-weight: 600; line-height: 1.15; }
  .person-name .credential { font-size: 28px; font-weight: 400; }
  .person-title { font-size: 25px; font-weight: 400; margin-top: 4px; color: #dfe8f5; }

  .brand-name {
    position: absolute; left: 40px; top: 335px; width: 400px;
    text-align: center; color: var(--brand-blue);
    font-size: 34px; font-weight: 700; line-height: 1.2;
    text-transform: uppercase; letter-spacing: 1px;
  }
  .divider {
    position: absolute; left: 470px; top: 290px;
    width: 2px; height: 200px; background: var(--divider);
  }
  .contact-block {
    position: absolute; left: 500px; top: 292px;
    color: var(--text-grey); font-size: 23px; line-height: 1.3;
  }
  .address { margin-bottom: 22px; }
  .contact-row { display: flex; align-items: center; gap: 12px; height: 34px; }
  .contact-row svg { width: 22px; height: 22px; flex: none; }
</style>
</head>
<body>
<div class="canvas">
  <div class="business-card">
    <header class="header-band">
      <div class="person-name">Marla Pennington, <span class="credential">CHRL</span></div>
      <div class="person-title">Leadership Coach</div>
    </header>

    <div class="brand-name">Red Stone<br>Leadership Coaching</div>

    <div class="divider"></div>

    <div class="contact-block">
      <div class="address">372 Fenwick Crescent<br>Oakville, Ontario, L6K 3R2</div>
      <div class="contact-row">
        <svg viewBox="0 0 22 22" aria-hidden="true"><rect x="6" y="2" width="10" height="18" rx="2" fill="none" stroke="var(--icon-blue)" stroke-width="2"/><circle cx="11" cy="16.5" r="1.2" fill="var(--icon-blue)"/></svg>
        <span>905-555-0148</span>
      </div>
      <div class="contact-row">
        <svg viewBox="0 0 22 22" aria-hidden="true"><rect x="2" y="5" width="18" height="12" rx="2" fill="var(--icon-blue)"/><path d="M3 6l8 6 8-6" fill="none" stroke="#fff" stroke-width="1.6"/></svg>
        <span>marla@redstoneleadcoach.example</span>
      </div>
      <div class="contact-row">
        <svg viewBox="0 0 22 22" aria-hidden="true"><circle cx="11" cy="11" r="9" fill="var(--icon-blue)"/><path d="M2 11h18M11 2c-4 5-4 13 0 18M11 2c4 5 4 13 0 18" fill="none" stroke="#fff" stroke-width="1.2"/></svg>
        <span>www.redstoneleadcoach.example</span>
      </div>
    </div>
  </div>
</div>
</body>
</html>
```